Law Enforcement SaaS

We're looking for a modern, somewhat minimalistic, business card layout to use for C-Suite interactions with customers in the public safety realm. We provide a patented information-sharing solution to law enforcement (can reference our company website at https://vornalux.com). The design should follow our current branding guide (attached as a reference with the logo) and focus on splashes of color to act as an accent. We intend to utilize the back of the card to highlight the product, and maybe insert a QR for our website. We're open to having a non-traditional design, so outside-the-box thinking is acceptable.

```html
<!DOCTYPE html>
<html lang="en">
<head>
<meta charset="utf-8">
<title>Vornalux Business Card</title>
<link rel="stylesheet" href="https://fonts.googleapis.com/css2?family=Montserrat:wght@400;600;800&display=swap">
<style>
  :root {
    --backdrop: #232323;
    --card: #ffffff;
    --ink: #111827;
    --accent: #35b6ea;
    --muted: #2b2f36;
  }
  * { box-sizing: border-box; margin: 0; padding: 0; }
  html, body {
    width: 1200px; height: 711px; overflow: hidden;
    background: var(--backdrop);
    font-family: "Montserrat", sans-serif;
    color: var(--ink);
  }
  .stage {
    position: relative; width: 1200px; height: 711px;
    display: flex; justify-content: center; align-items: center; gap: 90px;
  }
  .card {
    position: relative;
    width: 340px; height: 590px;
    background: var(--card);
    border-radius: 26px;
    box-shadow: 0 14px 30px rgba(0,0,0,.55);
  }

  /* Front */
  .front-lockup {
    position: absolute; left: 50%; top: 130px;
    transform: translateX(-50%);
    display: flex; flex-direction: column; align-items: center; gap: 24px;
  }
  .brand-dot {
    display: block;
    width: 58px; height: 58px; border-radius: 50%;
    background: var(--ink);
  }
  .front-name {
    writing-mode: vertical-rl;
    font-weight: 800; font-size: 40px; letter-spacing: 1px;
    color: var(--ink);
  }

  /* Back */
  .back-lockup {
    position: absolute; left: 0; right: 0; top: 52px;
    display: flex; flex-direction: column; align-items: center;
  }
  .back-lockup .brand-dot { width: 80px; height: 80px; }
  .back-name {
    margin-top: 26px;
    font-weight: 800; font-size: 36px; letter-spacing: 1px;
    color: var(--ink);
  }
  .person { position: absolute; top: 268px; left: 0; right: 0; text-align: center; }
  .person-name { font-weight: 600; font-size: 22px; color: var(--accent); letter-spacing: .5px; }
  .person-role { font-weight: 400; font-size: 13px; color: var(--muted); margin-top: 2px; }

  .divider {
    position: absolute; top: 346px; left: 30px; right: 30px;
    display: flex; align-items: center; gap: 8px;
  }
  .divider .rule { flex: 1; height: 2px; background: var(--accent); }
  .icon {
    width: 26px; height: 26px; border-radius: 7px;
    background: var(--accent);
    display: flex; align-items: center; justify-content: center;
  }
  .contacts {
    position: absolute; top: 384px; left: 0; right: 0;
    text-align: center; font-size: 13.5px; line-height: 21px; color: var(--muted);
  }
  .rule-full {
    position: absolute; top: 462px; left: 30px; right: 30px;
    height: 2px; background: var(--accent);
  }
  .address {
    position: absolute; top: 478px; left: 0; right: 0;
    text-align: center; font-size: 13.5px; line-height: 21px; color: var(--muted);
  }
</style>
</head>
<body>
<main class="stage">
  <section class="card card-front">
    <div class="front-lockup">
      <span class="brand-dot"></span>
      <span class="front-name">VORNALUX</span>
    </div>
  </section>

  <section class="card card-back">
    <div class="back-lockup">
      <span class="brand-dot"></span>
      <div class="back-name">VORNALUX</div>
    </div>

    <div class="person">
      <div class="person-name">MAREN HOLT</div>
      <div class="person-role">Managing Director</div>
    </div>

    <div class="divider">
      <span class="rule"></span>
      <span class="icon" aria-label="Phone">
        <svg width="16" height="16" viewBox="0 0 24 24"><path fill="#111827" d="M6.6 10.8a15 15 0 0 0 6.6 6.6l2.2-2.2a1 1 0 0 1 1-.25 11.4 11.4 0 0 0 3.6.57 1 1 0 0 1 1 1V20a1 1 0 0 1-1 1A17 17 0 0 1 3 4a1 1 0 0 1 1-1h3.5a1 1 0 0 1 1 1c0 1.25.2 2.45.57 3.57a1 1 0 0 1-.25 1z"/></svg>
      </span>
      <span class="icon" aria-label="Email">
        <svg width="16" height="16" viewBox="0 0 24 24"><path fill="#111827" d="M3 5h18v14H3z"/><path fill="none" stroke="#35b6ea" stroke-width="1.6" d="M3 6l9 7 9-7"/></svg>
      </span>
      <span class="icon" aria-label="Website">
        <svg width="16" height="16" viewBox="0 0 24 24"><circle cx="12" cy="12" r="9" fill="#111827"/><path fill="none" stroke="#35b6ea" stroke-width="1.4" d="M3 12h18M12 3c3 3 3 15 0 18M12 3c-3 3-3 15 0 18"/></svg>
      </span>
      <span class="rule"></span>
    </div>

    <div class="contacts">
      <div>123 456 789</div>
      <div>info@vornalux.com</div>
      <div>www.vornalux.com</div>
    </div>
    <div class="rule-full"></div>
    <div class="address">
      <div>Your address,</div>
      <div>City State, Zip 1234</div>
    </div>
  </section>
</main>
</body>
</html>
```